Web Design Project for NCYB

Hi,
I am looking for a website design for the Northern Council for Youth Boards.
This is an organisation which helps with legal disputes and other challenges which involve children.  The company want a web page which is professional but friendly.  The purpose of the website is to explain what the organisation does and to give people a place where they can download documents and information.
The homepage will have a video on the page.  ALSO, we would prefer the site to have a left hand navigation (not a top navigation).
I have enclosed the logo, a picture of the old (rubbish) home page and a screenshot from the video (you are welcome to change the dimensions).
If you have any questions, please ask.
-K
UPDATE: 6th DECEMBER:
Thanks for the designs so far.  I promise to give feedback to every single person.  In the meantime, can I just say that there's some good designs so far but I don't think anyone has nailed this yet.
So, I am uploading a screenshot called "theylikethis.jpg".  This is a screenshot from a website that the client says they like.
Can I also say, it's okay to reduce the size of the video.  I'm seeing a lot of massive videos.
Thanks folks!
UPDATE:  You can view a live demo of the site that they like at www.demohostqz.co.uk
UPDATE:  I've just found another good example of a site with a left nav at www.brightresourcehubnet.com

Hi,
Hi folks,
Had a quick look at the designs and just to say how impressed I am with the qualityand choice. There are a few that caught my eye and I'll try and narrow them down.I've also passed the link onto the other representatives for their input beforemaking a final choice. If I don't hear from any of the other represenatatives by Wednesday, I'll chose adesign and let you know. Once again many thanks for the quick response in gettingdesigns done and really looking forward to seeing the completed website.
Industry/Entity Type
Legal
Requirements
Must have
- a video player (any size of your choosing)
a left side navigation
the logo

```html
<!DOCTYPE html>
<html lang="en">
<head>
<meta charset="utf-8">
<title>NCYB – Northern Council for Youth Boards</title>
<link href="https://fonts.googleapis.com/css2?family=Cinzel:wght@400&family=Source+Sans+3:wght@400;600&family=Arimo:wght@400;700&display=swap" rel="stylesheet">
<style>
:root{
  --header-top:#0a3387;
  --header-bottom:#1f62c4;
  --brand-blue:#123f99;
  --nav-blue:#1a80cc;
  --nav-dark:#0d5aa8;
  --footer-blue:#0f85cc;
  --text-grey:#555555;
  --white:#ffffff;
}
*{margin:0;padding:0;box-sizing:border-box}
html,body{width:1200px;height:794px;overflow:hidden}
body{position:relative;background:linear-gradient(180deg,#e2e2e2 213px,#f6f6f6 470px,#fafafa 728px);font-family:"Arimo",Arial,sans-serif;color:var(--text-grey)}
.header-band{position:absolute;left:0;top:0;width:1200px;height:213px;background:linear-gradient(180deg,var(--header-top),var(--header-bottom))}
.brand{position:absolute;left:186px;top:30px;display:flex;align-items:center;gap:8px;color:var(--white);font-family:"Source Sans 3",sans-serif;font-weight:600;font-size:22px}
.brand-dot{width:14px;height:14px;border-radius:50%;background:var(--white)}
.site-title{position:absolute;left:294px;top:34px;color:var(--white);font-family:"Cinzel",serif;font-size:19px;letter-spacing:.5px}
.hero{position:absolute;left:183px;top:87px;width:837px;height:357px;background:#f4f4f4;border:1px solid #d8d8d8;box-shadow:0 14px 20px -12px rgba(0,0,0,.35)}
.hero-inner{position:absolute;left:10px;top:10px;width:816px;height:336px;background:var(--white);border:1px solid #e2e2e2;overflow:hidden}
.hero-photo{position:absolute;left:0;top:0;width:576px;height:336px;background:linear-gradient(90deg,#e9dcc6,#f3ece2 60%,#ffffff)}
.hero-copy{position:absolute;left:503px;top:108px;width:290px}
.hero-copy h1{font-family:"Source Sans 3",sans-serif;font-weight:400;line-height:1}
.hero-copy .line-a{display:block;font-size:24px;color:#111}
.hero-copy .line-b{display:block;font-size:34px;color:var(--brand-blue);margin-top:4px}
.hero-copy p{margin-top:12px;font-size:9.5px;line-height:15.5px;color:#666}
.slider-dots{position:absolute;left:361px;top:315px;height:22px;padding:0 8px;display:flex;gap:6px;align-items:center;background:#f1f1f1;border-radius:3px 3px 0 0}
.slider-dots span{width:11px;height:11px;border-radius:50%;background:#8c8c8c}
.slider-dots .active{background:#c0783e}
.side-nav{position:absolute;left:183px;top:482px;width:166px;height:225px;background:linear-gradient(180deg,#2490db,var(--nav-blue));border-radius:4px;box-shadow:0 2px 3px rgba(0,0,0,.3);padding-top:10px}
.side-nav a{display:block;height:23px;line-height:23px;padding-left:12px;color:var(--white);font-size:12px;text-decoration:none;text-shadow:0 1px 1px rgba(0,0,0,.3)}
.side-nav a.current{background:var(--nav-dark)}
.section-title{position:absolute;font-family:"Source Sans 3",sans-serif;font-weight:400;font-size:19px;color:var(--brand-blue)}
.video{position:absolute;left:379px;top:507px;width:235px;height:142px;background:#0c0c0c}
.video-screen{position:absolute;left:0;top:0;width:235px;height:128px;background:radial-gradient(circle at 50% 45%,#3a3a3a,#0c0c0c 70%)}
.video-bar{position:absolute;left:0;bottom:0;width:235px;height:14px;background:#1b1b1b;border-top:1px solid #444;font-size:4px;color:#aaa;padding:4px 0 0 30px}
.copy{position:absolute;font-size:9.5px;line-height:15.5px;color:var(--text-grey)}
.about-intro{position:absolute;left:645px;top:517px;width:138px;font-size:9px;line-height:15.5px;letter-spacing:-0.2px;color:var(--text-grey)}
.about-intro span{display:block;white-space:nowrap;text-align:justify;text-align-last:justify}
.about-intro span.last{text-align-last:left}
.about-photo{position:absolute;left:799px;top:520px;width:220px;height:90px;border:1px solid #ccc;background:linear-gradient(90deg,#ffffff,#f1e2cf 60%,#e8d4bc)}
.read-more{position:absolute;left:767px;top:658px;width:129px;height:28px;border-radius:3px;background:linear-gradient(180deg,#8a8a8a,#4e4e4e);color:var(--white);font-family:"Source Sans 3",sans-serif;font-size:15px;display:flex;align-items:center;justify-content:center;gap:8px;text-decoration:none}
.footer{position:absolute;left:0;top:728px;width:1200px;height:66px;background:var(--footer-blue);color:var(--white)}
.footer-links{position:absolute;left:195px;top:18px;font-size:9px;display:flex}
.footer-links a{color:var(--white);text-decoration:none}
.footer-links .sep{margin:0 9px}
.copyright{position:absolute;left:195px;top:37px;font-size:8.5px}
.connect{position:absolute;left:776px;top:18px;font-size:11px;line-height:15px}
.connect strong{font-weight:400;font-size:12.5px}
.socials{position:absolute;left:892px;top:20px;display:flex;gap:14px}
.socials span{display:flex;align-items:center;gap:4px;font-size:11px}
.socials i{width:12px;height:12px;border-radius:50%;background:var(--white);display:block}
</style>
</head>
<body>
<div class="header-band"></div>
<div class="brand"><span class="brand-dot"></span>NCYB</div>
<div class="site-title">Northern Council for Youth Boards</div>

<section class="hero">
  <div class="hero-inner">
    <div class="hero-photo" role="img" aria-label="Photo of a smiling mother with her young daughter"></div>
    <div class="hero-copy">
      <h1><span class="line-a">Northern Council</span><span class="line-b">for Youth Boards</span></h1>
      <p>Lorem Ipsum is simply dummy text of the printing and typesetting industry. Lorem Ipsum has been the industry's standard dummy text ever since the 1500s, when an unknown.</p>
    </div>
    <div class="slider-dots"><span></span><span></span><span class="active"></span><span></span><span></span><span></span></div>
  </div>
</section>

<nav class="side-nav">
  <a class="current" href="#">Home</a>
  <a href="#">About Us</a>
  <a href="#">News</a>
  <a href="#">Conferences</a>
  <a href="#">Minutes</a>
  <a href="#">Annual Report</a>
  <a href="#">Archive</a>
  <a href="#">Contact Us</a>
  <a href="#">Links</a>
</nav>

<h2 class="section-title" style="left:381px;top:478px">How it works</h2>
<div class="video">
  <div class="video-screen" role="img" aria-label="Video still of a presenter with a play button"></div>
  <svg style="position:absolute;left:94px;top:32px" width="48" height="48" viewBox="0 0 48 48"><circle cx="24" cy="24" r="22" fill="none" stroke="#777" stroke-width="2"/><path d="M19 15 L34 24 L19 33 Z" fill="#777"/></svg>
  <div style="position:absolute;left:0;top:84px;width:235px;text-align:center;font-weight:700;font-size:19px;color:#555">PLAY</div>
  <div class="video-bar">0:00 / 2:14</div>
</div>
<p class="copy" style="left:381px;top:658px;width:233px">Lorem Ipsum is simply dummy text of the printing and typesetting industry. Lorem Ipsum has been the industry's standard dummy.</p>

<h2 class="section-title" style="left:642px;top:484px">About NCYB</h2>
<p class="about-intro">
  <span>Lorem Ipsum is simply dummy</span>
  <span>text of the printing and typeset-</span>
  <span>ting industry. Lorem Ipsum has</span>
  <span>been the industry's standard</span>
  <span>dummy text ever since the</span>
  <span class="last">1500s,Lorem Ipsum is simply</span>
</p>
<div class="about-photo" role="img" aria-label="Photo of a mother holding her baby"></div>
<p class="copy" style="left:645px;top:614px;width:375px">Lorem Ipsum is simply dummy text of the printing and typesetting industry. Lorem Ipsum has been the industry's standard dummy text ever since the 1500s.</p>
<a class="read-more" href="#">Read More
  <svg width="18" height="12" viewBox="0 0 18 12"><path d="M1 1 L6 6 L1 11 M9 1 L14 6 L9 11" fill="none" stroke="#fff" stroke-width="2.5"/></svg></a>

<footer class="footer">
  <div class="footer-links">
    <a href="#">Home</a><span class="sep">|</span><a href="#">About Us</a><span class="sep">|</span><a href="#">News</a><span class="sep">|</span><a href="#">Conferences</a><span class="sep">|</span><a href="#">Minutes</a><span class="sep">|</span><a href="#">Annual Report</a><span class="sep">|</span><a href="#">Archive</a><span class="sep">|</span><a href="#">Contact Us</a><span class="sep">|</span><a href="#">Links</a>
  </div>
  <div class="copyright">© 2012 .NCYB. All Rights Reserved.</div>
  <div class="connect">Connect to<br><strong>our Social Network :</strong></div>
  <div class="socials"><span><i></i>Kite</span><span><i></i>Loop</span><span><i></i>Nest</span></div>
</footer>
</body>
</html>
```